Designing business cards for my start-up business

The company is called Velloran. We are a start-up tech data company based in Guernsey, Channel Islands. We want the business cards to look clean, fresh and innovative, just what a tech company should be. We do not want the business cards to look corporate or too official such as a bank. I would like the front of the business card to have our logo and the tag line of "Uniting Potential". On the back will be our contact details, emails etc. However I am open to your ideas and suggestions. I have provided all our logos and a word doc of all our contact details. There are 4 directors of the business, so I want 4 versions of the same design.

Target Market(s)

Our clients are businesses of all industries. Its a broad target market.

Industry/Entity Type

Information Technology

Contact Information for Business Card

I have attached a word doc called "Business Cards info" which gives all contact details of the 4 employees for the company.

Requirements
Must have
• We must have our logo and the tag line of "Uniting Potential". This could on the front of the card and then the individuals contact details on the back. Other than that, I'm happy for the designers to come up with ideas/styles.
Nice to have
• N/A
Should not have
• I don't want the cards to look too formal or corporate. As mentioned, we are a tech start-up so we want to look innovative.

```html
<!DOCTYPE html>
<html lang="en">
<head>
<meta charset="utf-8">
<title>Velloran Business Card</title>
<link rel="stylesheet" href="https://fonts.googleapis.com/css2?family=PT+Sans:ital,wght@0,400;0,700;1,400&display=swap">
<style>
  :root {
    --backdrop: #333333;
    --card: #fafafa;
    --accent: #f04a2c;
    --ink: #1c1c1c;
    --ink-soft: #555555;
    --rule: #cfcfcf;
  }
  * { margin: 0; padding: 0; box-sizing: border-box; }
  html, body {
    width: 1200px; height: 750px; overflow: hidden;
    background: var(--backdrop);
    font-family: "PT Sans", sans-serif;
  }
  .canvas { position: relative; width: 1200px; height: 750px; }
  .card {
    position: absolute; top: 228px;
    width: 462px; height: 263px;
    background: var(--card);
  }
  .card--details { left: 124px; }
  .card--brand { left: 618px; }

  /* details side */
  .brand-mini {
    position: absolute; left: 72px; top: 120px;
    display: flex; align-items: center; gap: 8px;
  }
  .brand-mini__square { width: 20px; height: 20px; background: var(--accent); }
  .brand-mini__name { font-size: 20px; font-weight: 700; color: var(--ink); }
  .divider {
    position: absolute; left: 206px; top: 48px;
    width: 1px; height: 168px; background: var(--rule);
  }
  .contact { position: absolute; left: 229px; top: 50px; }
  .contact__name { font-size: 18px; font-weight: 400; color: var(--accent); line-height: 22px; }
  .contact__role { font-size: 13.5px; color: var(--ink); line-height: 16px; }
  .contact__address {
    margin-top: 13px; font-size: 12.8px; color: var(--ink-soft);
    line-height: 17px; font-style: normal;
  }
  .contact__lines { list-style: none; margin-top: 7px; }
  .contact__line {
    display: flex; align-items: center; gap: 7px;
    font-size: 12.8px; color: var(--ink-soft); line-height: 19.5px;
  }
  .contact__line svg { width: 11px; height: 11px; flex: none; }

  /* brand side */
  .brand-main {
    position: absolute; left: 0; right: 0; top: 54px;
    display: flex; flex-direction: column; align-items: center;
  }
  .brand-main__square { width: 96px; height: 96px; background: var(--accent); margin-top: 14px; }
  .brand-main__name {
    margin-top: 26px; font-size: 20px; font-weight: 700;
    letter-spacing: 8px; color: var(--ink); padding-left: 8px;
  }
  .brand-main__tagline {
    margin-top: 16px; font-size: 13.5px; font-style: italic;
    letter-spacing: 1.2px; color: var(--ink);
  }
</style>
</head>
<body>
<main class="canvas">
  <section class="card card--details">
    <div class="brand-mini">
      <span class="brand-mini__square"></span>
      <span class="brand-mini__name">Velloran</span>
    </div>
    <div class="divider"></div>
    <div class="contact">
      <p class="contact__name">Elise Marchant</p>
      <p class="contact__role">Director</p>
      <address class="contact__address">
        14A Fermain Row, St Peter Port<br>
        Guernsey, GY1 4QX<br>
        Channel Islands
      </address>
      <ul class="contact__lines">
        <li class="contact__line">
          <svg viewBox="0 0 11 11" aria-hidden="true"><rect x="2" y="0.5" width="7" height="10" rx="1" fill="none" stroke="#f04a2c" stroke-width="1.2"/><rect x="4.3" y="8.3" width="2.4" height="0.9" fill="#f04a2c"/></svg>
          +44 7700 900 318
        </li>
        <li class="contact__line">
          <svg viewBox="0 0 11 11" aria-hidden="true"><rect x="0.5" y="2" width="10" height="7" fill="#f04a2c"/><path d="M0.5 2 L5.5 6 L10.5 2" fill="none" stroke="#fafafa" stroke-width="1"/></svg>
          Elise.Marchant@velloran.gg
        </li>
        <li class="contact__line">
          <svg viewBox="0 0 11 11" aria-hidden="true"><circle cx="5.5" cy="5.5" r="5" fill="#f04a2c"/><ellipse cx="5.5" cy="5.5" rx="2" ry="5" fill="none" stroke="#fafafa" stroke-width="0.8"/><line x1="0.5" y1="5.5" x2="10.5" y2="5.5" stroke="#fafafa" stroke-width="0.8"/></svg>
          www.velloran.gg
        </li>
      </ul>
    </div>
  </section>

  <section class="card card--brand">
    <div class="brand-main">
      <span class="brand-main__square"></span>
      <p class="brand-main__name">Velloran</p>
      <p class="brand-main__tagline">Uniting Potential</p>
    </div>
  </section>
</main>
</body>
</html>
```